Bright Robin Pet Sitting Postcard

I will be sending these postcards to homes in the neighborhood introducing my pet sitting business.

Include the following on the postcard:
Rosalind Mabry
738-405-2917
www.brightrobinpetsitting.example
help@brightrobinpetsitting.example

```html
<!DOCTYPE html>
<html lang="en">
<head>
<meta charset="utf-8">
<title>Bright Robin Pet Sitting Postcard</title>
<link href="https://fonts.googleapis.com/css2?family=Oswald:wght@500;600&family=Tinos:wght@400;700&display=swap" rel="stylesheet">
<style>
  :root {
    --navy: #3f6475;
    --navy-dark: #2f4f5e;
    --orange: #f7941d;
    --orange-deep: #ef6a1a;
    --yellow: #f6b40e;
    --white: #ffffff;
    --ink: #1f2a30;
    --page: #d5d9db;
    --line: #8a969c;
  }
  * { margin: 0; padding: 0; box-sizing: border-box; }
  html, body { width: 672px; height: 1200px; overflow: hidden; background: var(--page); }
  .canvas { position: relative; width: 672px; height: 1200px; }
  .postcard {
    position: absolute; left: 26px; width: 620px; height: 439px;
    overflow: hidden; background: var(--white);
    box-shadow: 0 6px 14px rgba(0,0,0,0.18);
    font-family: 'Tinos', serif;
  }
  .postcard--front { top: 110px; }
  .postcard--back { top: 652px; }
  .postcard svg.shapes { position: absolute; inset: 0; }

  /* front */
  .brand-mark {
    position: absolute; left: 34px; top: 40px; width: 150px; height: 92px;
    display: flex; align-items: center; justify-content: center; text-align: center;
    font-family: 'Tinos', serif; font-weight: 700; font-size: 21px; line-height: 1.1;
    color: var(--navy);
  }
  .headline {
    position: absolute; left: 236px; top: 14px; white-space: nowrap;
    font-family: 'Oswald', sans-serif; font-weight: 600; font-size: 35px; line-height: 1;
  }
  .headline .accent { color: var(--yellow); }
  .headline .main { color: var(--navy); }
  .tagline {
    position: absolute; left: 237px; top: 63px; width: 370px;
    font-size: 17.5px; line-height: 1.3; color: var(--ink);
  }
  .pill {
    position: absolute; height: 35px; border-radius: 18px;
    background: linear-gradient(180deg, var(--orange), var(--orange-deep));
    color: var(--white); font-weight: 700; display: flex; align-items: center; justify-content: center;
  }
  .pill--name { left: 23px; top: 353px; width: 269px; font-size: 27px; }
  .pill--phone { left: 323px; top: 353px; width: 270px; font-size: 31px; padding-left: 28px; }
  .pill--phone .phone-icon { position: absolute; left: 7px; top: 6px; width: 23px; height: 23px; }
  .front-link {
    position: absolute; top: 392px; color: var(--white); font-weight: 700; font-size: 14.5px;
    text-align: center; white-space: nowrap;
  }
  .front-link--web { left: 23px; width: 269px; }
  .front-link--mail { left: 323px; width: 270px; }
  .divider { position: absolute; left: 310px; top: 355px; width: 2px; height: 62px; background: var(--orange); }

  /* back */
  .services { position: absolute; left: 42px; top: 36px; }
  .services h2 {
    font-family: 'Oswald', sans-serif; font-weight: 500; font-size: 22px; color: var(--white);
    letter-spacing: 0.3px; margin-bottom: 4px;
  }
  .services h2 .accent { color: var(--yellow); font-weight: 600; }
  .services ul { list-style: none; }
  .services li {
    position: relative; padding-left: 28px; font-size: 20px; line-height: 33px; color: var(--white);
  }
  .services li svg { position: absolute; left: 0; top: 9px; width: 16px; height: 16px; }
  .mini-brand {
    position: absolute; left: 275px; top: 34px; width: 60px; height: 40px;
    display: flex; align-items: center; justify-content: center; text-align: center;
    font-size: 8.5px; font-weight: 700; line-height: 1.1; color: var(--navy);
  }
  .contact { position: absolute; left: 25px; top: 321px; }
  .contact .contact-name {
    font-size: 16.5px; font-weight: 700; color: var(--navy);
    width: 170px; padding-bottom: 4px; border-bottom: 1.5px solid var(--yellow); margin-bottom: 6px;
  }
  .contact ul { list-style: none; }
  .contact li { position: relative; padding-left: 29px; font-size: 15px; line-height: 20px; color: var(--ink); }
  .contact li svg { position: absolute; left: 1px; top: 3px; width: 14px; height: 14px; }
  .stamp-box { position: absolute; left: 524px; top: 23px; width: 70px; height: 68px; background: #ececec; border: 1.5px solid #cfcfcf; }
  .address-line { position: absolute; left: 382px; width: 211px; height: 1px; background: var(--line); }
</style>
</head>
<body>
<div class="canvas">

  <!-- Front of postcard -->
  <section class="postcard postcard--front">
    <svg class="shapes" viewBox="0 0 620 439" width="620" height="439">
      <defs>
        <linearGradient id="photoTone" x1="0" y1="0" x2="1" y2="0">
          <stop offset="0" stop-color="#d9cdb6"/>
          <stop offset="0.45" stop-color="#c9b596"/>
          <stop offset="0.75" stop-color="#7f8f5a"/>
          <stop offset="1" stop-color="#b48a4c"/>
        </linearGradient>
        <linearGradient id="topFade" x1="0" y1="0" x2="0" y2="1">
          <stop offset="0" stop-color="#ffffff" stop-opacity="0.97"/>
          <stop offset="0.8" stop-color="#ffffff" stop-opacity="0.9"/>
          <stop offset="1" stop-color="#ffffff" stop-opacity="0.6"/>
        </linearGradient>
      </defs>
      <rect role="img" aria-label="Photo of a ginger cat and a golden retriever sitting at a wooden dining table" x="0" y="0" width="620" height="360" fill="url(#photoTone)"/>
      <path d="M0 0 H620 V140 C540 150 470 150 400 142 C320 134 260 150 190 172 L0 172 Z" fill="url(#topFade)"/>
      <path d="M0 272 C40 320 120 345 230 345 C330 345 420 322 500 318 C560 315 600 322 620 326 V439 H0 Z" fill="var(--white)"/>
      <path d="M0 292 C50 333 130 352 235 350 C335 348 420 330 500 327 C560 325 600 330 620 334 V439 H0 Z" fill="var(--navy)"/>
      <circle cx="109" cy="86" r="112" fill="var(--navy)"/>
      <circle cx="109" cy="86" r="106" fill="none" stroke="var(--yellow)" stroke-width="3"/>
      <circle cx="109" cy="86" r="101" fill="var(--white)"/>
    </svg>
    <div class="brand-mark">Bright Robin<br>Pet Sitting</div>
    <h1 class="headline"><span class="accent">Bright Robin</span> <span class="main">Pet Sitting</span></h1>
    <p class="tagline">Do you worry about your pets when you are not home? Let us take that worry away!</p>
    <div class="pill pill--name">Rosalind Mabry</div>
    <div class="divider"></div>
    <div class="pill pill--phone">
      <svg class="phone-icon" viewBox="0 0 24 24"><circle cx="12" cy="12" r="12" fill="var(--navy)"/><path d="M8.2 6.5c.5-.4 1.1-.3 1.4.2l1.1 1.8c.3.5.2 1-.2 1.3l-.8.6c.5 1.3 1.6 2.5 2.9 3.1l.6-.8c.3-.4.9-.5 1.3-.2l1.8 1.1c.5.3.6 1 .2 1.4l-.9 1c-.6.6-1.5.8-2.3.5-3-1.1-5.2-3.4-6.3-6.3-.3-.8-.1-1.7.5-2.3z" fill="var(--white)"/></svg>
      738-405-2917
    </div>
    <div class="front-link front-link--web">www.brightrobinpetsitting.example</div>
    <div class="front-link front-link--mail">help@brightrobinpetsitting.example</div>
  </section>

  <!-- Back of postcard -->
  <section class="postcard postcard--back">
    <svg class="shapes" viewBox="0 0 620 439" width="620" height="439">
      <defs>
        <linearGradient id="catTone" x1="0" y1="0" x2="1" y2="1">
          <stop offset="0" stop-color="#8f7a6a"/><stop offset="1" stop-color="#4c4a47"/>
        </linearGradient>
        <linearGradient id="dogTone" x1="0" y1="0" x2="1" y2="1">
          <stop offset="0" stop-color="#e4e1dc"/><stop offset="1" stop-color="#3a3434"/>
        </linearGradient>
      </defs>
      <circle cx="160" cy="128" r="176" fill="none" stroke="var(--yellow)" stroke-width="6"/>
      <circle cx="160" cy="122" r="162" fill="var(--navy)"/>
      <circle cx="305" cy="54" r="41" fill="var(--yellow)"/>
      <circle cx="305" cy="54" r="37" fill="var(--white)"/>
      <circle cx="314" cy="181" r="60" fill="var(--yellow)"/>
      <circle cx="314" cy="181" r="57" fill="var(--navy)"/>
      <circle role="img" aria-label="Photo of a tabby cat resting on a rug" cx="314" cy="181" r="52" fill="url(#catTone)"/>
      <circle cx="265" cy="285" r="75" fill="var(--yellow)"/>
      <circle cx="265" cy="285" r="72" fill="var(--navy)"/>
      <circle role="img" aria-label="Photo of two dogs lying together on a bed" cx="265" cy="285" r="67" fill="url(#dogTone)"/>
    </svg>
    <div class="services">
      <h2><span class="accent">SERVICES</span> PROVIDED</h2>
      <ul>
        <li><svg viewBox="0 0 16 16"><circle cx="8" cy="8" r="8" fill="var(--yellow)"/><path d="M4.5 8.2l2.3 2.2 4.7-4.7" stroke="var(--navy)" stroke-width="1.8" fill="none"/></svg>Pet Sitting</li>
        <li><svg viewBox="0 0 16 16"><circle cx="8" cy="8" r="8" fill="var(--yellow)"/><path d="M4.5 8.2l2.3 2.2 4.7-4.7" stroke="var(--navy)" stroke-width="1.8" fill="none"/></svg>Almost Overnight</li>
        <li><svg viewBox="0 0 16 16"><circle cx="8" cy="8" r="8" fill="var(--yellow)"/><path d="M4.5 8.2l2.3 2.2 4.7-4.7" stroke="var(--navy)" stroke-width="1.8" fill="none"/></svg>Overnight</li>
        <li><svg viewBox="0 0 16 16"><circle cx="8" cy="8" r="8" fill="var(--yellow)"/><path d="M4.5 8.2l2.3 2.2 4.7-4.7" stroke="var(--navy)" stroke-width="1.8" fill="none"/></svg>Concierge Services</li>
        <li><svg viewBox="0 0 16 16"><circle cx="8" cy="8" r="8" fill="var(--yellow)"/><path d="M4.5 8.2l2.3 2.2 4.7-4.7" stroke="var(--navy)" stroke-width="1.8" fill="none"/></svg>Pet Taxi</li>
      </ul>
    </div>
    <div class="mini-brand">Bright Robin Pet Sitting</div>
    <div class="contact">
      <p class="contact-name">Rosalind Mabry</p>
      <ul>
        <li><svg viewBox="0 0 14 14"><circle cx="7" cy="7" r="7" fill="var(--navy)"/><path d="M4.8 3.8c.3-.2.6-.2.8.1l.6 1c.2.3.1.6-.1.8l-.5.3c.3.8.9 1.4 1.7 1.8l.3-.5c.2-.2.5-.3.8-.1l1 .6c.3.2.3.6.1.8l-.5.6c-.4.3-.9.4-1.3.3-1.7-.6-3-2-3.6-3.6-.2-.5-.1-1 .3-1.4z" fill="var(--white)"/></svg>738-405-2917</li>
        <li><svg viewBox="0 0 14 14"><circle cx="7" cy="7" r="7" fill="var(--navy)"/><circle cx="7" cy="7" r="4" fill="none" stroke="var(--white)" stroke-width="1"/><path d="M3 7h8M7 3c-1.5 2.5-1.5 5.5 0 8M7 3c1.5 2.5 1.5 5.5 0 8" fill="none" stroke="var(--white)" stroke-width="0.8"/></svg>www.brightrobinpetsitting.example</li>
        <li><svg viewBox="0 0 14 14"><circle cx="7" cy="7" r="7" fill="var(--navy)"/><rect x="3.6" y="4.6" width="6.8" height="4.8" fill="none" stroke="var(--white)" stroke-width="1"/><path d="M3.6 4.8L7 7.4l3.4-2.6" fill="none" stroke="var(--white)" stroke-width="1"/></svg>help@brightrobinpetsitting.example</li>
      </ul>
    </div>
    <div class="stamp-box"></div>
    <div class="address-line" style="top:199px"></div>
    <div class="address-line" style="top:260px"></div>
    <div class="address-line" style="top:322px"></div>
  </section>

</div>
</body>
</html>
```